BrightHaven Cleaning Services - inviting website needed to gain residential and commercial clients

Hello! I need a website for a newly created company that specializes in residential and commercial cleaning services. We clean homes, apartments, condos, rental apt for people that are too busy or don't want to spend time cleaning when they can be doing other things - whether that's because of long working hours or a business family schedule or perhaps for seniors that find it challenging to clean their homes.
In addition, for businesses we offer cleaning services of offices, doctors/dentist offices, essentially any business.
The company name is BrightHaven Cleaning Services which means we offer cleaning services not just inside homes and business but also outside. The outside services we offer include lawn mowing, pressure washing and snow removal.
I'm looking for a clean, contemporary design.
We are environmentally continuous and therefore use products that are not harmful to the environment, people or pets.
I should also mention that I would like to offer booking pages on the site as well so that clients can schedule their cleans and pay on line via credit card.
Website copy to be provided shortly but am hoping to see the initial design concept first?? Or if it helps, I can send copy in a few days

```html
<!DOCTYPE html>
<html lang="en">
<head>
<meta charset="utf-8">
<title>BrightHaven Cleaning Services</title>
<link href="https://fonts.googleapis.com/css2?family=Josefin+Sans:wght@400;600;700&family=Open+Sans:wght@400;600;700&display=swap" rel="stylesheet">
<style>
:root{
  --blue:#1b86d6;
  --blue-dark:#0d5fa8;
  --green:#3b9a2e;
  --green-dark:#237a1f;
  --ink:#222;
  --text:#666;
  --muted:#999;
  --soft:#f3f3f3;
  --tint:#eef6fc;
  --star:#f5b800;
  --white:#fff;
}
*{margin:0;padding:0;box-sizing:border-box}
html,body{width:1200px;height:4337px;overflow:hidden}
body{position:relative;background:var(--white);font-family:"Open Sans",sans-serif;color:var(--text)}
.abs{position:absolute}
h1,h2,h3,.head{font-family:"Josefin Sans",sans-serif;color:var(--ink)}

/* header */
.topline{left:0;top:0;width:1200px;height:5px;background:var(--blue)}
.header{left:0;top:5px;width:1200px;height:125px;background:var(--white);z-index:3}
.logo-disc{left:92px;top:-60px;width:200px;height:250px;border-radius:0 0 100px 100px;background:var(--white);z-index:4;display:flex;flex-direction:column;align-items:center;justify-content:flex-end;padding-bottom:56px}
.logo-mark{width:22px;height:22px;border-radius:50%;background:var(--green);margin-bottom:10px}
.logo-name{font-family:"Josefin Sans",sans-serif;font-weight:700;font-size:20px;color:var(--blue);text-align:center;line-height:1.2}
.call{right:100px;top:32px;font-size:17px;font-weight:600;color:var(--blue);display:flex;align-items:center;gap:10px}
.nav{right:90px;top:78px;display:flex;gap:46px;font-size:16px;font-weight:600;color:var(--ink);align-items:center}

/* hero */
.hero{left:0;top:130px;width:1200px;height:610px;background:linear-gradient(160deg,#8aa9c7 0%,#c9d8e6 40%,#e9eef3 70%,#b9c6d2 100%)}
.hero-curve{left:0;top:560px;width:1200px;height:190px}
.hero-title{left:96px;top:330px;font-size:46px;font-weight:400;color:var(--white)}
.hero-sub{left:96px;top:405px;font-size:17px;color:var(--white)}
.hero-btn{left:96px;top:462px;width:166px;height:52px;border:2px solid var(--white);border-radius:26px;color:var(--white);font-weight:700;font-size:15px;display:flex;align-items:center;justify-content:center}
.dots{left:555px;top:663px;display:flex;gap:10px}
.dots span{width:14px;height:14px;border-radius:50%;background:var(--white);border:2px solid #ccc}
.dots span.on{background:var(--blue);border-color:var(--blue)}

/* service cards */
.cards-bg{left:0;top:720px;width:1200px;height:330px;background:var(--soft)}
.card{width:465px;height:290px}
.card .txt{position:absolute;left:42px;color:var(--white)}
.card h3{font-size:25px;font-weight:600;color:var(--white);margin-bottom:14px}
.card p{font-size:13px;line-height:1.7;width:390px}
.card .more{font-size:13px;font-weight:700;margin-top:12px}

/* offer */
.sec-title{width:1200px;text-align:center;font-size:38px;font-weight:600}
.sec-sub{width:1200px;text-align:center;font-size:16px;color:#444}
.offer{top:1280px;left:115px;width:970px;display:flex;justify-content:space-between}
.offer-item{width:200px;text-align:center}
.offer-icon{width:116px;height:116px;border-radius:50%;border:2px solid #e2e2e2;margin:0 auto 28px;display:flex;align-items:center;justify-content:center}
.offer-item h4{font-size:16px;font-weight:600;color:var(--ink);margin-bottom:12px}
.offer-item p{font-size:13px;line-height:1.7;color:var(--muted)}
.offer-item .chev{margin-top:8px}
.arrow{font-size:30px;color:#333}

/* about */
.about-frame{left:515px;top:1657px;width:700px;height:512px;border-top:3px solid var(--green);border-left:3px solid var(--green);border-bottom:3px solid var(--green)}
.about-photo{left:0;top:1677px;width:600px;height:472px;background:linear-gradient(135deg,#6f8f5f 0%,#9fb08d 35%,#b6b9b6 60%,#8f969a 100%)}
.play{left:258px;top:1870px;width:80px;height:80px;border:3px solid var(--white);border-radius:50%}
.about-body{left:650px;top:1725px;width:440px}
.about-body h2{font-size:40px;font-weight:600;margin-bottom:34px}
.about-body p{font-size:13px;line-height:2.3;color:var(--muted);margin-bottom:10px}
.btn-blue{background:var(--blue);color:var(--white);font-weight:700;font-size:14px;border-radius:22px;display:flex;align-items:center;justify-content:center}

/* news */
.news{top:2386px;width:312px}
.news-photo{width:312px;height:194px;position:relative}
.news-date{position:absolute;left:0;bottom:0;padding:10px 16px;font-size:17px;font-weight:700;color:var(--white);background:rgba(0,0,0,.35);font-family:"Josefin Sans",sans-serif}
.news-row{display:flex;gap:14px;margin-top:30px}
.avatar{width:50px;height:50px;border-radius:50%;background:#c9a58c;flex:none}
.news-row h4{font-size:15px;font-weight:700;color:var(--ink);line-height:1.3;margin-bottom:8px}
.news-row p{font-size:12px;line-height:1.6;color:var(--muted)}
.news-more{margin:12px 0 0 64px;font-size:12px;color:var(--blue)}

/* testimonials */
.quotes-bg{left:0;top:2820px;width:1200px;height:500px;background:var(--tint)}
.quote{top:3040px;width:310px;display:flex;gap:18px}
.quote .avatar{width:72px;height:72px;border:4px solid var(--white)}
.quote p{font-size:13px;line-height:1.7;color:var(--muted)}
.quote p b{color:var(--blue);font-size:20px;margin-right:6px}
.quote .who{font-size:11px;color:#444;margin-top:12px;line-height:1.6}
.quote .who strong{font-weight:600;text-transform:uppercase;display:block}
.stars{color:var(--star);font-size:20px;letter-spacing:3px;margin-top:14px}
.circ-arrow{width:34px;height:34px;border-radius:50%;border:1px solid #bbb;color:#888;display:flex;align-items:center;justify-content:center;font-size:14px}

/* contact */
.contact{left:0;top:3311px;width:1200px;height:560px;background:linear-gradient(180deg,var(--blue) 0%,#1c7fcf 100%)}
.field{height:40px;background:var(--white);font-size:13px;color:#555;padding:11px 14px}
.send{left:483px;top:3715px;width:238px;height:40px;background:var(--green);color:var(--white);font-weight:700;font-size:15px;border-radius:4px;display:flex;align-items:center;justify-content:center;letter-spacing:.5px}

/* footer */
.foot-logo{left:75px;top:3940px;width:220px;text-align:center}
.foot-logo .logo-name{font-size:20px}
.social{display:flex;gap:10px;justify-content:center;margin-top:20px}
.social span{width:30px;height:30px;border-radius:50%;border:2px solid var(--blue)}
.foot-col h5{font-family:"Josefin Sans",sans-serif;font-size:17px;font-weight:600;color:var(--ink);margin-bottom:30px;letter-spacing:.5px}
.foot-col .line{display:flex;gap:14px;font-size:13px;color:#555;line-height:1.6;margin-bottom:22px}
.foot-col ul{list-style:none;font-size:13px;color:#555}
.foot-col li{margin-bottom:9px}
.foot-col li::before{content:"›";color:var(--blue);margin-right:12px;font-weight:700}
.email-in{width:300px;height:42px;border:1px solid #ccc;font-size:13px;padding:12px 14px;color:#555;margin:18px 0}
.copy{left:0;top:4251px;width:1200px;height:86px;border-top:1px solid #e6e6e6;text-align:center;padding-top:32px;font-size:13px;color:#444}
</style>
</head>
<body>

<div class="abs topline"></div>
<header class="abs header">
  <div class="abs call">
    <svg width="18" height="18" viewBox="0 0 24 24"><path fill="#1b86d6" d="M6.6 10.8a15 15 0 0 0 6.6 6.6l2.2-2.2c.3-.3.7-.4 1-.2 1.1.4 2.3.6 3.6.6.6 0 1 .4 1 1V20c0 .6-.4 1-1 1A17 17 0 0 1 3 4c0-.6.4-1 1-1h3.5c.6 0 1 .4 1 1 0 1.3.2 2.5.6 3.6.1.3 0 .7-.2 1z"/></svg>
    Schedule A Call : 1 888 888 8888
  </div>
  <nav class="abs nav">
    <span>Home</span><span>About Us</span><span>Services</span><span>Blog</span><span>Reviews</span><span>Contact Us</span>
    <svg width="16" height="16" viewBox="0 0 24 24"><circle cx="10" cy="10" r="7" fill="none" stroke="#1b86d6" stroke-width="3"/><path d="M15 15l6 6" stroke="#1b86d6" stroke-width="3"/></svg>
  </nav>
</header>
<div class="abs logo-disc">
  <span class="logo-mark"></span>
  <div class="logo-name">BrightHaven<br>Cleaning Services</div>
</div>

<section class="abs hero" role="img" aria-label="Photo of a wheel loader clearing snow on a wintry road"></section>
<div class="abs cards-bg"></div>
<svg class="abs hero-curve" viewBox="0 0 1200 190" preserveAspectRatio="none"><path d="M0 20 Q600 260 1200 20 L1200 190 L0 190 Z" fill="#f3f3f3"/></svg>
<h1 class="abs head hero-title">BrightHaven Cleaning Services</h1>
<p class="abs hero-sub">At vero eos etaccusamus et iusto odio dignissimos ducimus quiblanditiis</p>
<div class="abs hero-btn">READ MORE</div>
<div class="abs dots"><span class="on"></span><span></span><span></span><span></span></div>

<div class="abs card" style="left:107px;top:705px">
  <svg class="abs" width="465" height="290" viewBox="0 0 465 290"><defs><linearGradient id="gg" x1="0" y1="0" x2="1" y2="1"><stop offset="0" stop-color="#4aac33"/><stop offset="1" stop-color="#1f7a22"/></linearGradient></defs><path d="M0 0 Q232 60 465 0 L465 290 Q232 250 0 290 Z" fill="url(#gg)"/></svg>
  <div class="txt" style="top:92px">
    <h3>Residential Cleaning</h3>
    <p>Et harum quidem rerum facilis est et expedita distinam libero tem pore soluta nobis est elit optimque nihil impedit..</p>
    <div class="more">[Read More]</div>
  </div>
</div>
<div class="abs card" style="left:628px;top:705px;height:250px">
  <svg class="abs" width="465" height="250" viewBox="0 0 465 250"><defs><linearGradient id="bg" x1="0" y1="0" x2="1" y2="1"><stop offset="0" stop-color="#2a66c8"/><stop offset="1" stop-color="#1841a8"/></linearGradient></defs><path d="M0 60 Q232 0 465 0 L465 250 Q232 220 0 250 Z" fill="url(#bg)"/></svg>
  <div class="txt" style="top:110px">
    <h3>Commercial Cleaning</h3>
    <p>Et harum quidem rerum facilis est et expedita distinam libero tem pore soluta nobis est elit optimque nihil impedit..</p>
    <div class="more" style="text-align:right;width:390px">[Read More]</div>
  </div>
</div>

<h2 class="abs sec-title" style="left:0;top:1118px">What We Offer</h2>
<p class="abs sec-sub" style="left:0;top:1185px">We offer cleaning services not just inside homes and business but also outside.</p>
<div class="abs arrow" style="left:55px;top:1380px">‹</div>
<div class="abs arrow" style="left:1128px;top:1380px">›</div>
<div class="abs offer">
  <div class="offer-item">
    <div class="offer-icon"><svg width="60" height="50" viewBox="0 0 60 50" fill="none" stroke="#1b86d6" stroke-width="2.5"><path d="M6 6l14 22h26v10H14z"/><circle cx="18" cy="42" r="5"/><circle cx="42" cy="42" r="5"/></svg></div>
    <h4>Lawn mowing</h4>
    <p>Itaque earum rerum hic tenetur a sapiente delectut reiciendi</p>
    <div class="chev"><svg width="14" height="10"><path d="M2 2l5 5 5-5" stroke="#3b9a2e" stroke-width="2.5" fill="none"/></svg></div>
  </div>
  <div class="offer-item">
    <div class="offer-icon"><svg width="50" height="60" viewBox="0 0 50 60" fill="none" stroke="#1b86d6" stroke-width="2.5"><rect x="16" y="20" width="18" height="34" rx="3"/><path d="M25 20V6M18 6h14M34 28l10-6"/></svg></div>
    <h4>Pressure washing</h4>
    <p>Itaque earum rerum hic tenetur a sapiente delectut reiciendi</p>
    <div class="chev"><svg width="14" height="10"><path d="M2 2l5 5 5-5" stroke="#3b9a2e" stroke-width="2.5" fill="none"/></svg></div>
  </div>
  <div class="offer-item">
    <div class="offer-icon"><svg width="60" height="60" viewBox="0 0 60 60" fill="none" stroke="#1b86d6" stroke-width="2.5"><path d="M10 8l22 26M30 32l14 14M40 42l8-8 6 6-8 8z"/><circle cx="18" cy="44" r="6"/></svg></div>
    <h4>Snow removal</h4>
    <p>Itaque earum rerum hic tenetur a sapiente delectut reiciendi</p>
    <div class="chev"><svg width="14" height="10"><path d="M2 2l5 5 5-5" stroke="#3b9a2e" stroke-width="2.5" fill="none"/></svg></div>
  </div>
  <div class="offer-item">
    <div class="offer-icon"><svg width="60" height="60" viewBox="0 0 60 60" fill="none" stroke="#1b86d6" stroke-width="2.5"><path d="M30 6v28M18 34h24l4 16H14z"/></svg></div>
    <h4>Inside homes cleaning</h4>
    <p>Itaque earum rerum hic tenetur a sapiente delectut reiciendi</p>
    <div class="chev"><svg width="14" height="10"><path d="M2 2l5 5 5-5" stroke="#3b9a2e" stroke-width="2.5" fill="none"/></svg></div>
  </div>
</div>

<div class="abs about-frame"></div>
<div class="abs about-photo" role="img" aria-label="Photo of a worker pressure washing a paved patio"></div>
<div class="abs play"><svg width="74" height="74" viewBox="0 0 74 74"><path d="M30 23l22 14-22 14z" fill="#fff"/></svg></div>
<div class="abs about-body">
  <h2>About Us</h2>
  <p>At vero eos et accusamus et iusto odio dignissimos ducimus qui blanditiis praesentium voluptatum deleniti atque corrupti quos dolores et quas molestias excepturi sint occaecati cupiditate non provident, similique sunt in culpa qui officia deserunt laborum et dolorum fuga.</p>
  <p>Deleniti atque corrupti quos dolores et quas molestias excepturi sint occaecati cupiditate non provident, similique sunt in culpa qui officia deserunt laborum et dolorum fuga.</p>
</div>
<div class="abs btn-blue" style="left:650px;top:2052px;width:120px;height:42px">READ MORE</div>

<h2 class="abs sec-title" style="left:0;top:2292px">Latest News</h2>
<div class="abs" style="left:46px;top:2470px;font-size:30px;color:#ccc">‹</div>
<div class="abs" style="left:1136px;top:2470px;font-size:30px;color:#ccc">›</div>
<article class="abs news" style="left:101px">
  <div class="news-photo" role="img" aria-label="Photo of a cleaner wiping a kitchen counter" style="background:linear-gradient(135deg,#8b7a5c,#c9b98f 50%,#7f8a4a)"><span class="news-date">JUL 23, 2018</span></div>
  <div class="news-row"><span class="avatar"></span><div><h4>Temporibus autem quibusdam et autofficiis debitis..</h4><p>Sed ut perspiciatis unde omnis iste natus error sit voluptatem accusantium</p></div></div>
  <div class="news-more">Read More</div>
</article>
<article class="abs news" style="left:443px">
  <div class="news-photo" role="img" aria-label="Photo of a lawn mower on green grass" style="background:linear-gradient(135deg,#4f7a2b,#8fb34c 50%,#3c5f22)"><span class="news-date">MAY 23, 2018</span></div>
  <div class="news-row"><span class="avatar"></span><div><h4>Temporibus autem quibusdam et autofficiis debitis..</h4><p>Sed ut perspiciatis unde omnis iste natus error sit voluptatem accusantium</p></div></div>
  <div class="news-more">Read More</div>
</article>
<article class="abs news" style="left:787px">
  <div class="news-photo" role="img" aria-label="Photo of a cleaner mopping a bright room" style="background:linear-gradient(135deg,#d9d6cf,#f1efe9 50%,#b7b2a8)"><span class="news-date">JUL 23, 2018</span></div>
  <div class="news-row"><span class="avatar"></span><div><h4>Temporibus autem quibusdam et autofficiis debitis..</h4><p>Sed ut perspiciatis unde omnis iste natus error sit voluptatem accusantium</p></div></div>
  <div class="news-more">Read More</div>
</article>

<div class="abs quotes-bg"></div>
<h2 class="abs sec-title" style="left:0;top:2940px">What Customer says</h2>
<div class="abs circ-arrow" style="left:30px;top:3108px">‹</div>
<div class="abs circ-arrow" style="left:1133px;top:3108px">›</div>
<div class="abs quote" style="left:95px">
  <span class="avatar"></span>
  <div><p><b>“</b>At vero eos et accusamus et iusto odio dignissimos ducimus qui blan ditiipraesnt ium voluptat atuq.</p>
  <div class="who"><strong>Marla Vennick</strong>Financial Services Professional</div>
  <div class="stars">★★★★<span style="color:#ddd">☆</span></div></div>
</div>
<div class="abs quote" style="left:445px">
  <span class="avatar" style="background:#a9a9a9"></span>
  <div><p><b>“</b>At vero eos et accusamus et iustodio dignissimos ducimus qui blanditiipraesnt ium voluptat atuq.</p>
  <div class="who"><strong>Tobias R. Lindqvist</strong>National Urban Fellow at the Harbour</div>
  <div class="stars">★★★★★</div></div>
</div>
<div class="abs quote" style="left:790px">
  <span class="avatar" style="background:#d8bca6"></span>
  <div><p><b>“</b>At vero eos et accusamus et iusto odio dignissimos ducimus qui blan ditiipraesnt ium voluptat atuq.</p>
  <div class="who"><strong>Priya Halden</strong>Creative Strategist | Entrepreneur &amp; Upcoming</div>
  <div class="stars">★★★★<span style="color:#ddd">☆</span></div></div>
</div>

<section class="abs contact"></section>
<svg class="abs" style="left:0;top:3300px" width="1200" height="24" viewBox="0 0 1200 24" preserveAspectRatio="none"><path d="M0 24 L0 12 L60 6 L130 14 L210 4 L300 12 L390 6 L480 14 L560 5 L650 13 L740 6 L830 14 L920 4 L1010 12 L1100 6 L1200 12 L1200 24Z" fill="#1b86d6"/></svg>
<svg class="abs" style="left:0;top:3850px" width="1200" height="24" viewBox="0 0 1200 24" preserveAspectRatio="none"><path d="M0 0 L1200 0 L1200 10 L1120 18 L1030 8 L940 16 L850 6 L760 15 L670 7 L580 16 L490 8 L400 17 L310 7 L220 15 L130 8 L50 16 L0 10Z" fill="#1c7fcf"/></svg>
<h2 class="abs sec-title" style="left:0;top:3395px;color:#fff">Send us a Message</h2>
<div class="abs field" style="left:179px;top:3482px;width:411px">First Name</div>
<div class="abs field" style="left:179px;top:3534px;width:411px">Company Name</div>
<div class="abs field" style="left:179px;top:3586px;width:411px">Email Address</div>
<div class="abs field" style="left:179px;top:3638px;width:411px">Phone Number</div>
<div class="abs field" style="left:607px;top:3482px;width:411px">Last Name</div>
<div class="abs field" style="left:607px;top:3534px;width:411px;height:144px">Message :</div>
<div class="abs send">SEND MESSAGE</div>

<div class="abs foot-logo">
  <span class="logo-mark" style="display:inline-block"></span>
  <div class="logo-name">BrightHaven<br>Cleaning Services</div>
  <div class="social"><span></span><span></span><span></span></div>
</div>
<div class="abs foot-col" style="left:353px;top:3955px;width:240px">
  <h5>CONTACT US</h5>
  <div class="line"><svg width="14" height="18" viewBox="0 0 24 30"><path d="M12 0a10 10 0 0 0-10 10c0 8 10 20 10 20s10-12 10-20A10 10 0 0 0 12 0zm0 14a4 4 0 1 1 0-8 4 4 0 0 1 0 8z" fill="#1b86d6"/></svg><span>809 South e exentet ut eolupta temrepudiandae.</span></div>
  <div class="line"><svg width="14" height="14" viewBox="0 0 24 24"><path fill="#1b86d6" d="M6.6 10.8a15 15 0 0 0 6.6 6.6l2.2-2.2c.3-.3.7-.4 1-.2 1.1.4 2.3.6 3.6.6.6 0 1 .4 1 1V20c0 .6-.4 1-1 1A17 17 0 0 1 3 4c0-.6.4-1 1-1h3.5c.6 0 1 .4 1 1 0 1.3.2 2.5.6 3.6.1.3 0 .7-.2 1z"/></svg><span>Phone: (888) 888 - 8888</span></div>
  <div class="line"><svg width="14" height="12" viewBox="0 0 24 18"><path fill="#1b86d6" d="M0 0h24v18H0z"/><path d="M0 0l12 9 12-9" stroke="#fff" stroke-width="2" fill="none"/></svg><span>Email: info@companyname.com</span></div>
</div>
<div class="abs foot-col" style="left:654px;top:3955px;width:310px">
  <h5>SIGN UP FOR NEWSLETTER</h5>
  <p style="font-size:13px;color:#555;line-height:1.6">Want to make an impact? Provide your email and we'll be in touch.</p>
  <div class="email-in">Enter email</div>
  <div class="btn-blue" style="width:118px;height:40px;background:var(--green)">SIGN UP</div>
</div>
<div class="abs foot-col" style="left:1003px;top:3955px;width:160px">
  <h5>QUICK LINKS</h5>
  <ul><li>Home</li><li>About Us</li><li>Services</li><li>Blog</li><li>Reviews</li><li>Contact Us</li></ul>
</div>
<div class="abs copy">BrightHaven Cleaning Services. © 2018 All Rights Reserved | Privacy Policy | Terms and Conditions</div>

</body>
</html>
```